IT Consulting Site Revamping for Marlune

I've put a skeleton together on my website, but realize I need some help (it's http://pilot.marlune-example.ca).
I've pulled together tidbits from other websites, but really need my site to be cleaned up, and really spruced up.
I primarily focus on the IT needs of small to medium size businesses, taking care of everything from their servers and networks down to their workstations.
I also want a page listing the vendors (and logos) that I work with including Quillsoft, Zentrix, Halvor, Brax, TL, RZO, VELK, Trevo, Gatemoor.
There should also be a simple form to get a quote that will email me.
The final design should communicate strength and reliability.
I would like this to be a fully functional website, that I can upload to Plumly Pages, with the same sort of pages that are existing on http://pilot.marlune-example.ca
Updates
Hey everyone,
Hi everyone,
Reason: Hi all,
There are some designers that would like to submit some new designs, so I'm extending the deadline.
Thanks,
Target Market(s)
Small to medium size business owners. This will primarily be males who work in the oil and gas industry.
Industry/Entity Type
Consulting
Look and feel
Each slider illustrates characteristics of the customer's brand and the style your logo design should communicate.

```html
<!DOCTYPE html>
<html lang="en">
<head>
<meta charset="utf-8">
<title>Marlune Solutions</title>
<link href="https://fonts.googleapis.com/css2?family=Ubuntu:wght@400;500;700&display=swap" rel="stylesheet">
<style>
:root{
  --page:#ececec;
  --blue:#2a78b8;
  --blue-dark:#1f5f94;
  --text:#444;
  --heading:#555;
  --panel:#c6d7e2;
  --card:#e2e2e2;
  --nav-top:#f4f4f4;
  --nav-bottom:#cfcfcf;
  --footer:#c3d3de;
  --vendor-text:#555;
  --btn-slate:#5f7486;
  --btn-green:#3d9a2a;
  --btn-orange:#dd4d16;
  --btn-brown:#7e5216;
  --btn-blue:#2b6fa6;
}
*{box-sizing:border-box;margin:0;padding:0}
html,body{width:1085px;height:1200px;overflow:hidden}
body{background:var(--page);font-family:"Ubuntu",sans-serif;color:var(--text);position:relative}
.abs{position:absolute}

.brand{left:147px;top:30px;display:flex;align-items:center;gap:10px}
.brand-dot{width:44px;height:44px;border-radius:50%;background:var(--blue)}
.brand-name{font-size:36px;font-weight:700;color:var(--blue);letter-spacing:-0.5px}

.nav{left:140px;top:112px;width:805px;height:42px;background:linear-gradient(var(--nav-top),var(--nav-bottom));border-bottom:3px solid var(--blue)}
.nav a{position:absolute;top:12px;transform:translateX(-50%);font-size:13.5px;font-weight:700;color:var(--blue);text-decoration:none;white-space:nowrap}

.hero{left:140px;top:193px;width:805px;height:263px;background:var(--panel);border-bottom:3px solid var(--blue)}
.hero-photo{position:absolute;left:0;top:0;width:397px;height:260px;background:linear-gradient(120deg,#eef2f6 0%,#a9bfd6 45%,#5d7897 100%)}
.hero-caption{position:absolute;left:0;top:154px;width:397px;height:72px;background:rgba(52,112,168,.88);border-radius:0 4px 4px 0;padding:14px 14px;color:#fff;font-size:16.5px;font-weight:500;line-height:22px}
.hero-caption .c1{color:#c7ef3a}.hero-caption .c2{color:#ff8a2a}.hero-caption .c3{color:#ffee70}
.about{position:absolute;left:416px;top:20px;width:372px}
.about h2{font-size:14px;font-weight:500;color:var(--heading);margin-bottom:11px}
.about h2 span{color:var(--blue)}
.about p{font-size:12px;line-height:16.4px;color:#3c3c3c;margin-bottom:16px}
.btn{display:block;text-align:center;color:#fff;font-size:10.5px;border-radius:3px;text-decoration:none;box-shadow:inset 0 1px 0 rgba(255,255,255,.3)}
.about .btn{width:166px;height:24px;line-height:24px;background:linear-gradient(#3a86c4,var(--blue-dark));margin-top:-2px}

.section-title{left:139px;font-size:15px;font-weight:400;color:var(--heading);width:806px;padding-bottom:6px;border-bottom:3px solid var(--blue)}

.card{top:530px;width:145px;height:356px;background:var(--card);text-align:center}
.card-photo{height:144px}
.card h3{margin-top:12px;font-size:15px;font-weight:500;color:var(--heading);line-height:20.5px}
.card p{margin-top:13px;font-size:12px;line-height:16.3px;color:#555;padding:0 8px}
.card .btn{position:absolute;left:10px;top:319px;width:127px;height:22px;line-height:22px}

.vendor{top:976px;width:145px;height:140px;background:radial-gradient(#fafafa,#e2e2e2);border:1px solid #dedede;display:flex;align-items:center;justify-content:center;font-size:22px;font-weight:500;color:var(--vendor-text)}
.arrow{top:1030px}

.footer{left:140px;top:1155px;width:805px;height:25px;background:var(--footer);font-size:11px;color:#444;display:flex;justify-content:space-between;align-items:center;padding:0 9px 0 14px}
</style>
</head>
<body>

<div class="abs brand"><span class="brand-dot"></span><span class="brand-name">Marlune</span></div>

<nav class="abs nav">
  <a href="#" style="left:108px">HOME</a>
  <a href="#" style="left:251px">OUR SERVICES</a>
  <a href="#" style="left:393px">ABOUT US</a>
  <a href="#" style="left:536px">OUR PRODUCTS</a>
  <a href="#" style="left:678px">CONTACT US</a>
</nav>

<section class="abs hero">
  <div class="hero-photo" role="img" aria-label="Photo of two technicians working among server racks in a data centre"></div>
  <div class="hero-caption">Small Business Information Technology Services<br><span class="c1">Easy,</span> <span class="c2">Affordable</span> and <span class="c3">Reliable.</span></div>
  <div class="about">
    <h2>About <span>Marlune Solutions</span></h2>
    <p>Marlune Solutions is a computer solutions provider and IT consulting firm that supports a wide variety of local small businesses in the Calgary area primarily. Our company also provides IT services to businesses throughout Alberta on special projects.</p>
    <p>Marlune has been trusted for over the last 7 years by small business companies like yours. Whether you are looking for an ongoing computer support company, looking to outsource your small business computer work, or just looking for a computer company to help you solve a computer problem, Marlune is your right choice.</p>
    <a class="btn" href="#">read more about us</a>
  </div>
</section>

<h2 class="abs section-title" style="top:492px">Our Services</h2>

<div class="abs card" style="left:139px">
  <div class="card-photo" role="img" aria-label="Photo of a technician on the phone checking network cabling in a server rack" style="background:linear-gradient(135deg,#f2f2f2,#9aa4ad)"></div>
  <h3>MANAGED IT<br>SERVICES</h3>
  <p>Lorem ipsum dolor sit amet, consectetur adipiscing elit. Nunc vulputate pretium vehicula. Ut a tristique magna.</p>
  <a class="btn" href="#" style="background:linear-gradient(#7a8fa1,var(--btn-slate))">more about it</a>
</div>
<div class="abs card" style="left:305px">
  <div class="card-photo" role="img" aria-label="Close-up photo of an open hard disk platter and read head" style="background:linear-gradient(135deg,#c9d3de,#3d5f9a)"></div>
  <h3>STORAGE AND<br>VIRTUALIZATION</h3>
  <p>Lorem ipsum dolor sit amet, consectetur adipiscing elit. Nunc vulputate pretium vehicula. Ut a tristique magna.</p>
  <a class="btn" href="#" style="background:linear-gradient(#56b83e,var(--btn-green))">more about it</a>
</div>
<div class="abs card" style="left:470px">
  <div class="card-photo" role="img" aria-label="Photo of a businessman holding a glowing globe" style="background:linear-gradient(135deg,#1e3a5c,#5a8fc4)"></div>
  <h3>NETWORKING<br>SERVICES</h3>
  <p>Lorem ipsum dolor sit amet, consectetur adipiscing elit. Nunc vulputate pretium vehicula. Ut a tristique magna.</p>
  <a class="btn" href="#" style="background:linear-gradient(#f0682e,var(--btn-orange))">more about it</a>
</div>
<div class="abs card" style="left:635px">
  <div class="card-photo" role="img" aria-label="Close-up photo of a USB drive and memory card on a disc" style="background:linear-gradient(135deg,#6c5a3a,#c89a4a)"></div>
  <h3>BACKUP AND<br>RECOVERY</h3>
  <p>Lorem ipsum dolor sit amet, consectetur adipiscing elit. Nunc vulputate pretium vehicula. Ut a tristique magna.</p>
  <a class="btn" href="#" style="background:linear-gradient(#9a6a26,var(--btn-brown))">more about it</a>
</div>
<div class="abs card" style="left:799px">
  <div class="card-photo" role="img" aria-label="Photo of a hard drive with a stethoscope on a white background" style="background:linear-gradient(135deg,#ffffff,#d8d8c8)"></div>
  <h3>COMPUTER<br>RERPAIR SERVICES</h3>
  <p>Lorem ipsum dolor sit amet, consectetur adipiscing elit. Nunc vulputate pretium vehicula. Ut a tristique magna.</p>
  <a class="btn" href="#" style="background:linear-gradient(#3b85c2,var(--btn-blue))">more about it</a>
</div>

<h2 class="abs section-title" style="top:921px">Vendors</h2>

<svg class="abs arrow" style="left:105px" width="20" height="28" viewBox="0 0 20 28"><path d="M15 3 L5 14 L15 25" fill="none" stroke="#3b7fbf" stroke-width="4" stroke-linecap="round"/></svg>
<div class="abs vendor" style="left:139px">Quillsoft</div>
<div class="abs vendor" style="left:305px">Zentrix</div>
<div class="abs vendor" style="left:470px">Halvor</div>
<div class="abs vendor" style="left:635px">Brax</div>
<div class="abs vendor" style="left:799px">TL</div>
<svg class="abs arrow" style="left:962px" width="20" height="28" viewBox="0 0 20 28"><path d="M5 3 L15 14 L5 25" fill="none" stroke="#3b7fbf" stroke-width="4" stroke-linecap="round"/></svg>

<footer class="abs footer"><span>2012 © Marlune Solutions</span><span>All Rights Reserved</span></footer>

</body>
</html>
```